Gazebrix fresh re-design

We are UK based company and have Magento website which we are happy with, but we require fresh design. Menu must be customer friendly

Design must reflect in strength as strength of our products and value for money are our selling points.

Our products are not family products there mainly used for business at events, cycling, running clubs, etc

New design must have same information as current design

links that require new design

http://www.gazebrix.example (landing page)

http://www.gazebrix.example/3m-x-3m-heavy-duty-tents/3m-x-3m-pop-up-marquee-white.html (product page)

http://www.gazebrix.example/custom-design-own-tent-size/choose-3mx3m.html (design tool)

Target Market(s)

business owners, cycling clubs, running clubs,

Industry/Entity Type

It Company

Number of Pages Required

3 page

Requirements
Must have
• background image of working gazebrix, clean fresh design, printed gazebrixes eg. cupcake
Should not have
• all same functions as current page

```html
<!DOCTYPE html>
<html lang="en">
<head>
<meta charset="utf-8">
<title>Gazebrix – Pop Up Marquees and Gazebos</title>
<link rel="stylesheet" href="https://fonts.googleapis.com/css2?family=Raleway:wght@400;500;600;700;800&family=Open+Sans:wght@400;600;700&display=swap">
<style>
:root{
  --red:#e8121b;
  --red-dark:#c50d15;
  --blue:#1d3a8f;
  --navy:#0f2a7a;
  --ink:#222;
  --text:#555;
  --muted:#888;
  --line:#dcdcdc;
  --nav:#6e6e6e;
  --hero:#e4e4e4;
  --soft:#f0eff0;
  --footer:#111;
  --white:#fff;
}
*{box-sizing:border-box;margin:0;padding:0}
html,body{width:1200px;height:3659px;overflow:hidden}
body{font-family:"Open Sans",Arial,sans-serif;color:var(--text);background:var(--white);font-size:14px}
section,header,footer,nav{position:relative;width:1200px}
.wrap{position:absolute;left:49px;right:49px}
.btn{display:inline-block;font-family:"Raleway",Arial,sans-serif;font-weight:700;font-size:15px;text-transform:uppercase;padding:16px 30px}

/* header */
.site-header{height:141px}
.toplinks{position:absolute;right:50px;top:10px;font-size:12px;color:var(--muted);white-space:nowrap}
.toplinks .first{color:var(--red)}
.toplinks span{margin:0 6px}
.brand{position:absolute;left:52px;top:50px;display:flex;align-items:center;gap:12px}
.brand-square{width:30px;height:30px;background:var(--red);display:block}
.brand-name{font-family:"Raleway",Arial,sans-serif;font-weight:800;font-size:38px;color:var(--blue)}
.search{position:absolute;left:395px;top:62px;display:flex}
.search-input{width:361px;height:36px;border:1px solid var(--line);font-size:11px;color:#aaa;padding:10px 14px}
.search-btn{width:78px;height:36px;background:var(--red);color:#fff;font-size:12px;font-weight:700;display:flex;align-items:center;justify-content:center}
.cart{position:absolute;left:983px;top:62px;width:168px;height:36px;border:1px solid var(--line);display:flex;align-items:center;gap:10px;padding:0 12px;font-size:11px;color:var(--ink)}

/* nav */
.main-nav{height:50px;background:var(--nav)}
.main-nav ul{list-style:none;position:absolute;left:60px;top:0;height:50px;display:flex;align-items:center}
.main-nav li{color:#fff;font-size:12px;font-weight:600;margin-right:48px;display:flex;align-items:center}
.checkout{position:absolute;right:49px;top:0;width:104px;height:50px;background:var(--red);color:#fff;font-size:12px;font-weight:700;display:flex;align-items:center;justify-content:center;gap:8px}

/* hero */
.hero{height:516px;background:var(--hero)}
.hero-title{position:absolute;left:52px;top:150px;font-family:"Raleway",Arial,sans-serif;font-weight:800;font-size:66px;line-height:1;color:var(--blue)}
.hero-title em{font-style:normal;color:var(--red)}
.hero-sub{position:absolute;left:52px;top:228px;font-family:"Raleway",Arial,sans-serif;font-weight:500;font-size:40px;color:var(--red)}
.hero-sub em{font-style:normal;color:var(--blue)}
.hero-copy{position:absolute;left:52px;top:290px;width:580px;font-size:13px;line-height:1.7;color:#444}
.dots{position:absolute;left:52px;top:420px;display:flex;gap:8px}
.dots i{width:14px;height:14px;border-radius:50%;border:2px solid var(--red)}
.dots i.on{background:var(--red)}
.hero-photo{position:absolute;left:646px;top:42px;width:500px;height:463px;background:linear-gradient(170deg,#2b43b8 0%,#2a3fa6 32%,#cfd2d8 33%,#b9bcc4 100%)}

/* features */
.features{height:123px;background:#f4f4f4;border-bottom:1px solid #e5e5e5}
.features .wrap{top:22px;display:flex;height:78px}
.feature{flex:1;display:flex;align-items:center;gap:18px;padding-left:12px;border-right:1px solid var(--line)}
.feature:last-child{border-right:0}
.feature-icon{width:56px;height:56px;border-radius:50%;border:1px solid var(--line);background:#fff;display:flex;align-items:center;justify-content:center}
.feature b{display:block;font-family:"Raleway",Arial,sans-serif;font-size:18px;color:var(--red);font-weight:700;text-transform:uppercase}
.feature span{font-size:12px;color:var(--muted)}

/* promos */
.promos{height:440px}
.promo-red{position:absolute;left:49px;top:24px;width:427px;height:397px;background:var(--red);text-align:center;color:#fff;padding-top:46px}
.promo-red h2{font-family:"Raleway",Arial,sans-serif;font-weight:800;font-size:54px;line-height:1.05}
.promo-red p{font-size:13px;line-height:1.5;margin:16px 40px 30px}
.promo-red .btn{background:#fff;color:var(--red)}
.promo-dark{position:absolute;left:507px;top:24px;width:649px;height:397px;background:linear-gradient(160deg,#3a3a3a,#1e1e1e 60%,#2b2b2b);text-align:center;color:#fff;padding-top:60px}
.promo-dark h2{font-family:"Raleway",Arial,sans-serif;font-weight:800;font-size:54px;line-height:1}
.promo-dark .off{display:inline-block;background:#c9c9c9;color:var(--red);font-family:"Raleway",Arial,sans-serif;font-weight:800;font-size:48px;padding:0 34px;margin-top:2px;line-height:1.1}
.promo-dark p{font-size:13px;line-height:1.5;margin:20px 70px 26px}
.promo-dark .btn{background:var(--navy);color:#fff}

/* design band */
.design-band{height:417px;background:linear-gradient(180deg,#3a4350 0%,#4f555d 55%,#3b3e43 100%);text-align:center;color:#fff}
.design-band h2{position:absolute;left:0;right:0;top:110px;font-family:"Raleway",Arial,sans-serif;font-weight:600;font-size:50px}
.design-band p{position:absolute;left:95px;right:95px;top:208px;font-size:13px;line-height:1.7}
.design-band .btn{position:absolute;left:483px;top:302px;background:var(--red);color:#fff}

/* products */
.products{height:708px;background:var(--soft)}
.products-head{position:absolute;left:49px;right:49px;top:36px;height:40px;border-bottom:1px solid var(--line)}
.products-head h2{font-family:"Raleway",Arial,sans-serif;font-weight:600;font-size:24px;color:var(--ink)}
.products-head h2 em{font-style:normal;color:var(--red)}
.filters{position:absolute;right:0;top:4px;display:flex;gap:8px}
.filters span{border:1px solid var(--line);background:#fff;font-size:10px;font-weight:700;padding:3px 8px;color:var(--muted)}
.filters span.active{color:var(--red)}
.card{position:absolute;top:93px;width:254px;height:463px;background:#fff;padding:16px 14px}
.card-photo{height:175px}
.sale{position:absolute;right:14px;top:8px;background:var(--red);color:#fff;font-size:10px;font-weight:700;padding:2px 8px}
.price{font-family:"Raleway",Arial,sans-serif;font-size:36px;color:var(--ink);margin-top:18px}
.price small{font-size:16px}
.card h3{font-size:13px;font-weight:400;color:var(--red);margin-top:12px}
.card p{font-size:13px;line-height:1.5;color:#444;margin-top:12px}
.card-actions{position:absolute;left:14px;bottom:20px;display:flex;gap:18px}
.cart-btn{width:52px;height:52px;background:var(--red);display:flex;align-items:center;justify-content:center}
.more-btn{width:112px;height:52px;background:#e6e6e6;border:1px solid #ccc;color:#666;font-size:14px;display:flex;align-items:center;justify-content:center}
.pager{position:absolute;right:49px;top:615px;display:flex;gap:6px;align-items:center;font-size:14px}
.pager span{height:28px;min-width:28px;display:flex;align-items:center;justify-content:center}
.pager .cur{background:var(--navy);color:#fff}
.pager .pg{background:#ccc;color:#444}
.pager .next{background:#8a8a8a;color:#fff;padding:0 14px}

/* seo */
.about{height:334px;text-align:center}
.about h2{position:absolute;left:0;right:0;top:60px;font-family:"Raleway",Arial,sans-serif;font-weight:600;font-size:34px;color:var(--red)}
.about h2 em{font-style:normal;color:var(--navy)}
.about h4{position:absolute;left:0;right:0;top:128px;font-size:14px;font-weight:600;color:var(--navy)}
.about p{position:absolute;left:95px;right:95px;font-size:11px;line-height:1.9;color:#666}

/* newsletter */
.newsletter{height:197px;background:#7d7d7d;color:#fff}
.newsletter h2{position:absolute;left:52px;top:60px;font-family:"Raleway",Arial,sans-serif;font-weight:600;font-size:34px}
.newsletter p{position:absolute;left:52px;top:110px;width:320px;font-size:12px;line-height:1.4}
.news-input{position:absolute;left:398px;top:62px;width:574px;height:72px;background:#666;border:1px solid #8d8d8d;font-size:13px;padding:26px 30px;color:#ddd}
.news-btn{position:absolute;left:972px;top:62px;width:180px;height:72px;background:var(--red);font-family:"Raleway",Arial,sans-serif;font-weight:800;font-size:22px;display:flex;align-items:center;justify-content:center}

/* social */
.social{height:234px;text-align:center}
.social h2{position:absolute;left:0;right:0;top:40px;font-family:"Raleway",Arial,sans-serif;font-weight:600;font-size:26px;color:var(--red)}
.social-item{position:absolute;top:110px;width:214px}
.social-btn{height:50px;color:#fff;font-weight:700;font-size:18px;display:flex;align-items:center;justify-content:center;gap:12px}
.social-btn i{width:14px;height:14px;border-radius:50%;border:2px solid #fff}
.social-item span{display:block;margin-top:12px;font-size:12px;color:var(--muted)}

/* guarantees */
.guarantees{height:134px;background:var(--red);display:flex;color:#fff}
.guarantee{flex:1;display:flex;align-items:center;justify-content:center;gap:20px;border-right:1px solid rgba(255,255,255,.35);font-family:"Raleway",Arial,sans-serif;font-weight:700;font-size:17px;line-height:1.3;text-transform:uppercase}
.guarantee:last-child{border-right:0}

/* footer */
.site-footer{height:342px;background:var(--footer);color:#aaa}
.footer-col{position:absolute;top:60px}
.footer-col h5{color:#fff;font-size:13px;font-weight:700;margin-bottom:22px}
.footer-col li{list-style:none;font-size:11px;line-height:2.1;text-transform:uppercase}
.contact-row{display:flex;gap:10px;font-size:11px;line-height:1.6;margin-bottom:14px;text-transform:uppercase}
.footer-bottom{position:absolute;left:0;right:0;bottom:0;height:60px;border-top:1px solid #2a2a2a}
.copyright{position:absolute;left:62px;top:22px;font-size:11px}
.cards{position:absolute;right:52px;top:16px;display:flex;gap:6px}
.cards i{width:40px;height:26px;border-radius:3px;display:block}
</style>
</head>
<body>

<header class="site-header">
  <div class="toplinks"><span class="first">LOGIN/REGISTER</span>|<span>MY ACCOUNT</span>|<span>WISHLIST - 0</span></div>
  <div class="brand"><i class="brand-square"></i><span class="brand-name">Gazebrix</span></div>
  <div class="search"><div class="search-input">Enter keyword</div><div class="search-btn">SEARCH</div></div>
  <div class="cart">
    <svg width="20" height="18" viewBox="0 0 20 18"><path d="M1 2h3l2.5 9h10l2-7H5.5" fill="none" stroke="#e8121b" stroke-width="2"/><circle cx="8" cy="15" r="1.6" fill="#e8121b"/><circle cx="15" cy="15" r="1.6" fill="#e8121b"/></svg>
    <span>CART :</span><span style="color:#888">0 (items)</span>
    <svg width="10" height="6" viewBox="0 0 10 6" style="margin-left:auto"><path d="M0 0h10L5 6z" fill="#888"/></svg>
  </div>
</header>

<nav class="main-nav">
  <ul>
    <li><svg width="20" height="18" viewBox="0 0 20 18"><path d="M10 1L1 9h3v8h4v-5h4v5h4V9h3z" fill="#fff"/></svg></li>
    <li>GAZEBRIXES</li><li>ROOFS</li><li>WALLS</li><li>GAZEBO WEIGHTS</li><li>GUTTERS</li><li>SANDBAGS</li><li>TABLES</li><li>PARTS</li>
  </ul>
  <div class="checkout">CHECKOUT <svg width="14" height="12" viewBox="0 0 14 12"><path d="M0 4h8V0l6 6-6 6V8H0z" fill="#fff"/></svg></div>
</nav>

<section class="hero">
  <h1 class="hero-title">THE <em>STRONGEST</em></h1>
  <div class="hero-sub">GAZEBRIXES <em>IN THE WORLD</em></div>
  <p class="hero-copy">Lorem ipsum dolor sit amet, consectetur adipiscing elit, sed do eiusmod tempor incididunt ut labore et dolore magna aliqua. Lorem ipsum dolor sit amet, consectetur adipiscing elit, sed do eiusmod tempor incididunt ut labore et dolore magna aliqua.</p>
  <div class="dots"><i class="on"></i><i></i><i></i><i></i></div>
  <div class="hero-photo" role="img" aria-label="Blue heavy duty gazebrix standing open beside its folded frame and carry bag"></div>
</section>

<section class="features">
  <div class="wrap">
    <div class="feature"><div class="feature-icon"><svg width="26" height="26" viewBox="0 0 26 26"><path d="M3 11h5v12H3zM10 23V11l5-9c2 0 3 1 3 3l-1 5h6c1 0 2 1 2 2l-2 9c0 1-1 2-2 2z" fill="none" stroke="#e8121b" stroke-width="2" stroke-linejoin="round"/></svg></div><div><b>Satisfaction</b><span>100% Guaranteed</span></div></div>
    <div class="feature"><div class="feature-icon"><svg width="28" height="22" viewBox="0 0 28 22"><path d="M1 3h16v13H1zM17 8h6l4 5v3H17z" fill="#e8121b"/><circle cx="6" cy="18" r="3" fill="#e8121b" stroke="#fff" stroke-width="1.5"/><circle cx="22" cy="18" r="3" fill="#e8121b" stroke="#fff" stroke-width="1.5"/></svg></div><div><b>Free Shipping</b><span>on orders over $99</span></div></div>
    <div class="feature"><div class="feature-icon"><svg width="26" height="26" viewBox="0 0 26 26"><path d="M21 9a9 9 0 0 0-16-1M5 17a9 9 0 0 0 16 1" fill="none" stroke="#e8121b" stroke-width="3"/><path d="M22 2v8h-8zM4 24v-8h8z" fill="#e8121b"/></svg></div><div><b>7 Day</b><span>Easy to Return Items</span></div></div>
    <div class="feature"><div class="feature-icon"><svg width="26" height="26" viewBox="0 0 26 26"><circle cx="13" cy="13" r="11" fill="none" stroke="#e8121b" stroke-width="3"/><circle cx="13" cy="13" r="5" fill="none" stroke="#e8121b" stroke-width="3"/></svg></div><div><b>Support</b><span>Customer Service</span></div></div>
  </div>
</section>

<section class="promos">
  <div class="promo-red">
    <h2>NEW<br>ARRIVALS</h2>
    <p>Lorem ipsum dolor sit amet conse ctetur adipisicing elit, sed do eiusmod tempor incididunt ut labore et dolore magna aliqua.</p>
    <span class="btn">SHOP NOW</span>
  </div>
  <div class="promo-dark" role="img" aria-label="Dimly lit event hall with gazebrix frames in the background">
    <h2>LATEST PRODUCT</h2>
    <div class="off">25% OFF</div>
    <p>Lorem ipsum dolor sit amet conse ctetur adipisicing elit, sed do eiusmod tempor incididunt ut labore et dolore magna aliqua.</p>
    <span class="btn">SHOP NOW</span>
  </div>
</section>

<section class="design-band" role="img" aria-label="Printed gazebrixes set up at an outdoor event beside parked cars">
  <h2>DESIGN YOUR OWN GAZEBRIX</h2>
  <p>Lorem ipsum dolor sit amet, consectetur adipiscing elit, sed do eiusmod tempor incididunt ut labore et dolore magna aliqua. Ut enim ad minim veniam, quis nostrud exercitation ullamco laboris nisi ut aliquip ex ea commodo consequat. Duis aute irure dolor in reprehenderit in voluptate.</p>
  <span class="btn">SHOP NOW</span>
</section>

<section class="products">
  <div class="products-head">
    <h2><em>NEW</em> PRODUCT</h2>
    <div class="filters"><span class="active">PRICE ▾</span><span>CATEGORY ▾</span><span>BRAND ▾</span></div>
  </div>

  <article class="card" style="left:49px">
    <span class="sale">Sale !</span>
    <div class="card-photo" role="img" aria-label="White pop-up gazebrix with side walls on grass" style="background:linear-gradient(180deg,#5a6a5a 0%,#e9ecef 35%,#dfe3e6 65%,#5d7a43 100%)"></div>
    <div class="price">$ 449.00 <small>ex vat</small></div>
    <h3>3m x 3m Heavy Duty Pop-Up White</h3>
    <p>Lorem ipsum dolor sit amet, edit consectetur adipiscing elit,</p>
    <div class="card-actions"><div class="cart-btn"><svg width="24" height="22" viewBox="0 0 20 18"><path d="M1 2h3l2.5 9h10l2-7H5.5" fill="none" stroke="#fff" stroke-width="2"/><circle cx="8" cy="15" r="1.6" fill="#fff"/><circle cx="15" cy="15" r="1.6" fill="#fff"/></svg></div><div class="more-btn">MORE</div></div>
  </article>

  <article class="card" style="left:334px">
    <span class="sale">Sale !</span>
    <div class="card-photo" role="img" aria-label="Orange pop-up gazebrix on a lawn" style="background:linear-gradient(180deg,#4f6048 0%,#f08a1c 30%,#e67e12 62%,#5f8a3c 100%)"></div>
    <div class="price">$ 449.00 <small>ex vat</small></div>
    <h3>3m x 3m Heavy Duty Pop-Up White</h3>
    <p>Lorem ipsum dolor sit amet, edit consectetur adipiscing elit,</p>
    <div class="card-actions"><div class="cart-btn"><svg width="24" height="22" viewBox="0 0 20 18"><path d="M1 2h3l2.5 9h10l2-7H5.5" fill="none" stroke="#fff" stroke-width="2"/><circle cx="8" cy="15" r="1.6" fill="#fff"/><circle cx="15" cy="15" r="1.6" fill="#fff"/></svg></div><div class="more-btn">MORE</div></div>
  </article>

  <article class="card" style="left:620px">
    <span class="sale">Sale !</span>
    <div class="card-photo" role="img" aria-label="White gazebrix with windowed walls on grass" style="background:linear-gradient(180deg,#7d8a78 0%,#eef0f1 35%,#e3e6e8 68%,#678a47 100%)"></div>
    <div class="price">$ 449.00 <small>ex vat</small></div>
    <h3>3m x 3m Heavy Duty Pop-Up White</h3>
    <p>Lorem ipsum dolor sit amet, edit consectetur adipiscing elit,</p>
    <div class="card-actions"><div class="cart-btn"><svg width="24" height="22" viewBox="0 0 20 18"><path d="M1 2h3l2.5 9h10l2-7H5.5" fill="none" stroke="#fff" stroke-width="2"/><circle cx="8" cy="15" r="1.6" fill="#fff"/><circle cx="15" cy="15" r="1.6" fill="#fff"/></svg></div><div class="more-btn">MORE</div></div>
  </article>

  <article class="card" style="left:903px">
    <span class="sale">Sale !</span>
    <div class="card-photo" role="img" aria-label="Yellow gazebrix leg weight on grass" style="background:radial-gradient(circle at 50% 70%,#e8c51e 0 18%,transparent 19%),linear-gradient(180deg,#8a9a6c,#6f8d45)"></div>
    <div class="price">$ 449.00 <small>ex vat</small></div>
    <h3>3m x 3m Heavy Duty Pop-Up White</h3>
    <p>Lorem ipsum dolor sit amet, edit consectetur adipiscing elit,</p>
    <div class="card-actions"><div class="cart-btn"><svg width="24" height="22" viewBox="0 0 20 18"><path d="M1 2h3l2.5 9h10l2-7H5.5" fill="none" stroke="#fff" stroke-width="2"/><circle cx="8" cy="15" r="1.6" fill="#fff"/><circle cx="15" cy="15" r="1.6" fill="#fff"/></svg></div><div class="more-btn">MORE</div></div>
  </article>

  <div class="pager"><span class="cur">1</span><span class="pg">2</span><span>............</span><span class="next">Next</span></div>
</section>

<section class="about">
  <h2><em>Pop</em> Up Marquees and Gazebos for <em>Sale</em></h2>
  <h4>Mini Pop Up Marquees and Gazebos with sides</h4>
  <p style="top:172px">Pop up marquees and heavy duty gazebos for sale near you! At Gazebrix we have expanded our markets to different countries and our pop up marquees and heavy duty gazebos are now available for delivery in several European countries, so your wait is over. All you have to do now is order your instant awnings from the Gazebrix website. Please note we deliver to Ireland and all over Europe.</p>
  <p style="top:246px">Our pop up marquees and heavy duty gazebos are the best on the web and are durable enough to last for years. Gazebrix offers a large range of coloured mini pop up marquees. Heavy duty gazebos and instant awnings are built to satisfy customers by providing them with the best quality products. All our pop up marquees and heavy duty gazebos are available on our website and you can order them right away.</p>
</section>

<section class="newsletter">
  <h2>Newsletter Sign Up</h2>
  <p>Lorem ipsum dolor sit amet, conse ctetur adipisicing elit, sed do eiusmod tempor incididunt ut labore</p>
  <div class="news-input">Enter Your E-Mail Id</div>
  <div class="news-btn">SUBSCRIBE</div>
</section>

<section class="social">
  <h2>FOLLOW US TO STAY IN TOUCH</h2>
  <div class="social-item" style="left:110px"><div class="social-btn" style="background:#1f5fb8"><i></i>Facefeed</div><span>1234 Like</span></div>
  <div class="social-item" style="left:380px"><div class="social-btn" style="background:#2aa3e0"><i></i>Chirper</div><span>1234 Followers</span></div>
  <div class="social-item" style="left:642px"><div class="social-btn" style="background:#1d4e6a"><i></i>Worknet</div><span>1234 Connections</span></div>
  <div class="social-item" style="left:904px"><div class="social-btn" style="background:#e23a45"><i></i>Circles Plus</div><span>123 Connections</span></div>
</section>

<section class="guarantees">
  <div class="guarantee"><svg width="44" height="44" viewBox="0 0 26 26"><path d="M3 11h5v12H3zM10 23V11l5-9c2 0 3 1 3 3l-1 5h6c1 0 2 1 2 2l-2 9c0 1-1 2-2 2z" fill="#fff"/></svg><span>Satisfaction<br>100% Guaranteed</span></div>
  <div class="guarantee"><svg width="48" height="38" viewBox="0 0 28 22"><path d="M1 3h16v13H1zM17 8h6l4 5v3H17z" fill="#fff"/><circle cx="6" cy="18" r="3" fill="#fff" stroke="#e8121b" stroke-width="1.5"/><circle cx="22" cy="18" r="3" fill="#fff" stroke="#e8121b" stroke-width="1.5"/></svg><span>Free Shipping<br>on orders over $99</span></div>
  <div class="guarantee"><svg width="42" height="42" viewBox="0 0 26 26"><path d="M21 9a9 9 0 0 0-16-1M5 17a9 9 0 0 0 16 1" fill="none" stroke="#fff" stroke-width="3"/><path d="M22 2v8h-8zM4 24v-8h8z" fill="#fff"/></svg><span>7 Day<br>Easy Return</span></div>
</section>

<footer class="site-footer">
  <div class="footer-col" style="left:66px"><h5>INFORMATION</h5><ul><li>About Us</li><li>Customer Service</li><li>Privacy Policy</li><li>Search Terms</li><li>Orders and Returns</li><li>Contact Us</li></ul></div>
  <div class="footer-col" style="left:338px"><h5>WHY BUY FROM US</h5><ul><li>Shipping &amp; Returns</li><li>Secure Shopping</li><li>International Shipping</li><li>Affiliates</li><li>Group Sales</li></ul></div>
  <div class="footer-col" style="left:638px"><h5>MY ACCOUNT</h5><ul><li>Sign In</li><li>View Cart</li><li>My Wishlist</li><li>Track My Order</li><li>Help</li></ul></div>
  <div class="footer-col" style="left:883px"><h5>CONTACTS</h5>
    <div class="contact-row"><svg width="12" height="16" viewBox="0 0 12 16"><path d="M6 0a6 6 0 0 0-6 6c0 4 6 10 6 10s6-6 6-10a6 6 0 0 0-6-6zm0 8.5A2.5 2.5 0 1 1 6 3.5a2.5 2.5 0 0 1 0 5z" fill="#aaa"/></svg><span>12 Harbour Lane, Dunmore DM4 7QX<br>P. O Box 25994, Country</span></div>
    <div class="contact-row"><svg width="12" height="14" viewBox="0 0 12 14"><path d="M2 0l3 3-1.5 2c1 2 2.5 3.5 4.5 4.5L10 8l2 3-2 3C5 13 0 7 0 2z" fill="#aaa"/></svg><span>Call us: (800) 555-0147</span></div>
    <div class="contact-row"><svg width="14" height="11" viewBox="0 0 14 11"><path d="M0 0h14v11H0z" fill="#aaa"/><path d="M0 0l7 6 7-6" fill="none" stroke="#111" stroke-width="1.4"/></svg><span>Email: hello@gazebrix.example</span></div>
  </div>
  <div class="footer-bottom">
    <div class="copyright">All Rights Reserved, Copyrights © 2015</div>
    <div class="cards"><i style="background:#fff"></i><i style="background:#f0f0f0"></i><i style="background:#e8e8e8"></i></div>
  </div>
</footer>

</body>
</html>
```